Flyer Design

We are a new charity. Our immediate aim is to respond to the ebola crisis in Sierra Leone. We need a flier or a booklet to inform and raise funds.

Industry/Entity Type

Charity

Requirements
Must have
• The donation page and the gift aid form should be at the back and in a back and front format.
Nice to have
• Front page with our best photo

```html
<!DOCTYPE html>
<html lang="en">
<head>
<meta charset="utf-8">
<title>Gift Aid Declaration Flyer</title>
<link href="https://fonts.googleapis.com/css2?family=Open+Sans:wght@400;600;700&display=swap" rel="stylesheet">
<style>
  :root {
    --bg: #8a8a8a;
    --brand-blue: #2b9fd8;
    --panel: #ffffff;
    --ink: #2a2a2a;
    --rule: #444444;
    --photo-warm: #9a7a5a;
    --photo-dark: #4a3a2a;
  }
  * { box-sizing: border-box; margin: 0; padding: 0; }
  html, body {
    width: 1200px; height: 900px; overflow: hidden;
    background: var(--bg);
    font-family: "Open Sans", sans-serif;
    color: var(--ink);
  }
  .flyer {
    position: absolute; left: 270px; top: 30px;
    width: 660px; height: 840px;
    background: var(--brand-blue);
    border-radius: 14px;
    padding: 18px;
    display: flex; flex-direction: column;
  }
  .flyer__photo {
    height: 330px;
    border-radius: 14px 14px 0 0;
    background: linear-gradient(160deg, #6b5a45 0%, var(--photo-warm) 45%, #b89a78 70%, var(--photo-dark) 100%);
  }
  .flyer__title {
    color: #fff; font-weight: 700; font-size: 15.5px;
    text-align: center; letter-spacing: 0.2px;
    padding: 9px 0 8px;
  }
  .form-panel {
    position: relative; flex: 1;
    background: var(--panel);
    border-radius: 4px 4px 24px 24px;
    padding: 18px 26px 20px;
    font-size: 12.2px; line-height: 1.42;
    overflow: hidden;
  }
  .form-panel p { margin-bottom: 6px; }
  .form-panel .caps { font-weight: 600; }
  .field {
    display: inline-block; border-bottom: 1px solid var(--rule);
    height: 13px; vertical-align: baseline;
  }
  .row { display: flex; gap: 8px; margin-bottom: 9px; align-items: baseline; }
  .row .field { flex: 1; }
</style>
</head>
<body>
  <article class="flyer">
    <div class="flyer__photo" role="img" aria-label="Photograph of two smiling children carrying water containers on their heads in a village"></div>
    <h1 class="flyer__title">GIFT AID DECLARATION – FOR PAST, PRESENT &amp; FUTURE DONATIONS</h1>
    <section class="form-panel">
      <div class="row">Name of charity or Community Amateur Sports Club <span class="field"></span></div>
      <p class="caps">PLEASE TREAT AS GIFT AID DONATIONS ALL QUALIFYING GIFTS OF MONEY MADE</p>
      <div class="row">today <span class="field" style="flex:0 0 70px"></span> in the past 4 years <span class="field" style="flex:0 0 90px"></span> in the future <span class="field" style="flex:0 0 110px"></span></div>
      <p>Please tick all boxes you wish to apply.<br>
      I confirm I have paid or will pay an amount of Income Tax and/or Capital Gains Tax for each tax year (6 April to 5 April) that is at least equal to the amount of tax that all the charities or Community Amateur Sports Clubs (CASCs) that I donate to will reclaim on my gifts for that tax year. I understand that other taxes such as VAT and Council Tax do not qualify. I understand the charity will reclaim 28p of tax on every £1 that I gave up to 5 April 2008 and will reclaim 25p of tax on every £1 that I give on or after 6 April 2008.<br>
      Donor’s details</p>
      <div class="row">Title <span class="field" style="flex:0 0 50px"></span> First name or initial(s) <span class="field"></span> Surname <span class="field"></span></div>
      <div class="row">Full home address <span class="field"></span></div>
      <div class="row"><span class="field"></span> Postcode <span class="field" style="flex:0 0 120px"></span></div>
      <div class="row">Date <span class="field"></span> Signature <span class="field"></span></div>
      <p>Please notify the charity or CASC if you: Want to cancel this declaration | Change your name or home address | No longer pay sufficient tax on your income and/or capital gains.</p>
      <p>If you pay Income Tax at the higher or additional rate and want to receive the additional tax relief due to you, you must include all your Gift Aid donations on your Self Assessment tax return or ask HM Revenue and Customs to adjust your tax code</p>
    </section>
  </article>
</body>
</html>
```